Wall Backdrop - Fern Hollow Roastery -

See the attached logo and wall dimensions. The dimensions are in "inches" We are looking for the backdrop that customers will see walking up to the front of the Roastery. For design we are located in the pacific northwest along the coastal hwy 101 and in the heart of the Tamarack Ridge State Forest. The Roastery will be located in the Fern Hollow Casino. Web site www.fernhollowcasino.example . We want the back drop to be inviting an can encompass the beautiful nature in the area or a warm, friendly coffee shop.
Updates

The RED X's on the mural wall need to be cut out. No art in the red X areas.

Target Market(s)

50+ in Age, coffee drinkers

Industry/Entity Type

Entertainment

Requirements
Must have
• The Roastery Logo but background doesn't need to match the logo colors
Nice to have
• Something that tells the eyes to have a cup of coffee

```html
<!DOCTYPE html>
<html lang="en">
<head>
<meta charset="utf-8">
<title>Fern Hollow Roastery – Wall Backdrop</title>
<link rel="stylesheet" href="https://fonts.googleapis.com/css2?family=Open+Sans:wght@600&display=swap">
<style>
  :root {
    --page: #ffffff;
    --roast-deep: #0e0604;
    --roast-mid: #2b130c;
    --roast-warm: #3a1a10;
    --cutout: #ffffff;
    --logo-ink: #f4f2ef;
    --cup-light: #e4e2df;
    --cup-dark: #2a140e;
  }
  html, body {
    margin: 0;
    padding: 0;
    width: 1200px;
    height: 1200px;
    overflow: hidden;
    background: var(--page);
  }
  .canvas {
    position: relative;
    width: 1200px;
    height: 1200px;
  }
  .mural-wall {
    position: absolute;
    left: 26px;
    top: 378px;
    width: 1147px;
    height: 443px;
    overflow: hidden;
  }
  .bean-backdrop {
    position: absolute;
    inset: 0;
    background: radial-gradient(ellipse at 45% 30%, var(--roast-warm) 0%, var(--roast-mid) 45%, var(--roast-deep) 100%);
  }
  .cutout {
    position: absolute;
    background: var(--cutout);
  }
  .cutout--door {
    left: 88px;
    top: 86px;
    width: 468px;
    height: 357px;
  }
  .cutout--window {
    left: 688px;
    top: 195px;
    width: 233px;
    height: 115px;
    z-index: 2;
  }
  .roastery-mark {
    position: absolute;
    left: 625px;
    top: 50px;
    width: 460px;
    height: 60px;
    display: flex;
    align-items: center;
    gap: 14px;
  }
  .roastery-mark__dot {
    flex: none;
    width: 44px;
    height: 44px;
    border-radius: 50%;
    background: var(--logo-ink);
  }
  .roastery-mark__name {
    margin: 0;
    font-family: "Open Sans", sans-serif;
    font-weight: 600;
    font-size: 31px;
    letter-spacing: 0.5px;
    line-height: 1;
    color: var(--logo-ink);
    white-space: nowrap;
  }
  .coffee-cup {
    position: absolute;
    left: 850px;
    top: 146px;
    width: 270px;
    height: 270px;
    border-radius: 50%;
    background: radial-gradient(circle, var(--cup-dark) 0%, var(--cup-dark) 45%, var(--cup-light) 100%);
    z-index: 1;
  }
</style>
</head>
<body>
  <main class="canvas">
    <section class="mural-wall">
      <div class="bean-backdrop" role="img" aria-label="Dark roasted coffee beans filling the wall backdrop"></div>
      <div class="cutout cutout--door" aria-hidden="true"></div>
      <div class="roastery-mark">
        <span class="roastery-mark__dot" aria-hidden="true"></span>
        <h1 class="roastery-mark__name">FERN HOLLOW ROASTERY</h1>
      </div>
      <div class="coffee-cup" role="img" aria-label="Photograph of a white cup of black coffee seen from above"></div>
      <div class="cutout cutout--window" aria-hidden="true"></div>
    </section>
  </main>
</body>
</html>
```